HomePage Design for Lumen Getaways - once-in-a-lifetime experiences for busy working people

Design a homepage for the Lumen Getaways (www.lumengetaways.example) website compatible with further web pages and the design briefing documents attached

LG HomePage Design Brief
We are seeking website HomePage designs incorporating our new Logo and colour scheme, for Lumen Getaways (www.lumengetaways.example) to go with the site functionality and wireframe ideas attached.
The website HomePage design needs to
• Incorporate and be consistent with the LG Logo and its colour scheme attached.
• Express the brand values of being inspirational, high quality, upscale, cultured, aspirational, and contemporary – even somewhat ‘hip’. Probably positioned somewhere between Harlow Pike (Deluxe Travel) and Green Walrus (Hip Travel) – see https://www.harlowpike.example and https://www.greenwalrus.example .
• Be instantly recognisable and different from other travel websites and instantly communicate the nature of the brand proposition and target customer base.
• Appeal to our core 25-55 affluent businesspeople demographic
• Work in the UK, US/Canada and Australia/NZ and ultimately in mainland Europe.
• Use fonts and colours that are easily reproduced online and compatible with nearly all browsers.
• Be part of a responsive website design, that can be used both on Desktops and laptops but also with tablets and mobile ‘phones (hence content not too wide across the page)
• Feature the strapline ‘Lumen Getaways in less than 7 Days’
• Work with the and wireframes and processes shown in the attached presentation – although intended as a guide only these features and processes all need to be incorporated into the HomePage.
• Make full use of high quality images and video to convey our brand proposition and products

Target Market(s)

25-55 affluent businesspeople

Industry/Entity Type

Travel Industry

Number of Pages Required

1 page

Font styles to use
Sans Serif

Colors
0455a3
00a88f

Requirements
Must have
• • Incorporate and be consistent with the LG Logo and its colour scheme attached.
• • Express the brand values of being inspirational, high quality, upscale, cultured, aspirational, and contemporary – even somewhat ‘hip’. Probably positioned somewhere between Harlow Pike (Deluxe Travel) and Green Walrus (Hip Travel) – see https://www.harlowpike.example and https://www.greenwalrus.example .
• • Be instantly recognisable and different from other travel websites and instantly communicate the nature of the brand proposition and target customer base.
• • Appeal to our core 25-55 affluent businesspeople demographic
• • Be part of a responsive website design, that can be used both on Desktops and laptops but also with tablets and mobile ‘phones (hence content not too wide across the page)
• • Feature the strapline ‘Lumen Getaways in less than 7 Days’
• • Work with the and wireframes and processes shown in the attached presentation – although intended as a guide only these features and processes all need to be incorporated into the HomePage.
• • Make full use of high quality images and video to convey our brand proposition and products
• Colours as per Logo not as shown below
Nice to have
• • Work in the UK, US/Canada and Australia/NZ and ultimately in mainland Europe.
Should not have
• Must not be cheap or mass-market, nor excessively "stuffy or luxury-orientated"

```html
<!DOCTYPE html>
<html lang="en">
<head>
<meta charset="utf-8">
<title>Lumen Getaways – Home</title>
<link rel="stylesheet" href="https://fonts.googleapis.com/css2?family=Lato:wght@300;400;700&family=Asap+Condensed:wght@500;600&display=swap">
<style>
  :root {
    --page-white: #ffffff;
    --band-grey: #e8e8e8;
    --ink: #1d1d1d;
    --ink-soft: #3a3a3a;
    --label-white: #ffffff;
    --tag-yellow: #f5f200;
    --tag-ink: #1a1a1a;
    --btn-book: #27326f;
    --btn-offers: #1e5b2c;
    --play-fill: #ffffff;
    --play-mark: #555555;
  }
  html, body {
    margin: 0;
    padding: 0;
    width: 1200px;
    height: 1200px;
    overflow: hidden;
    background: var(--page-white);
    font-family: "Lato", Arial, sans-serif;
    color: var(--ink);
  }
  .page { position: relative; width: 1200px; height: 1200px; }

  .experiences {
    position: absolute; left: 0; top: 6px; width: 1200px; height: 602px;
    background: var(--band-grey);
  }
  .section-title {
    position: absolute; margin: 0;
    font-size: 22px; font-weight: 300; letter-spacing: 0.2px;
    white-space: nowrap; transform: translateX(-50%);
  }
  .section-title strong { font-weight: 400; }
  .experiences .section-title { left: 605px; top: 40px; }

  .tile {
    position: absolute; width: 228px; height: 212px; overflow: hidden;
  }
  .tile-label {
    position: absolute; left: 0; right: 0; bottom: 14px;
    font-family: "Asap Condensed", "Arial Narrow", sans-serif;
    font-weight: 500; font-size: 16.5px; line-height: 21px;
    color: var(--label-white); text-align: center;
    text-shadow: 0 1px 3px rgba(0,0,0,0.75);
  }
  .tile-shade {
    position: absolute; left: 0; right: 0; bottom: 0; height: 70px;
    background: linear-gradient(to bottom, rgba(0,0,0,0), rgba(0,0,0,0.45));
  }
  .tile--wildlife { left: 107px; top: 104px; background: linear-gradient(160deg, #5f7a2a, #6e6a4e 55%, #3f4a22); }
  .tile--festivals { left: 362px; top: 104px; background: linear-gradient(135deg, #c23a8f, #e07a3a 50%, #f2a21a); }
  .tile--activities { left: 616px; top: 104px; background: linear-gradient(180deg, #4b4a40, #b9c3c8 35%, #d9dee0); }
  .tile--events { left: 870px; top: 104px; background: linear-gradient(180deg, #3f7a4a, #5a3a5a 60%, #20202e); }
  .tile--places { left: 238px; top: 343px; background: linear-gradient(170deg, #a33a22, #c9693a 50%, #d9a058); }
  .tile--performances { left: 493px; top: 343px; background: linear-gradient(180deg, #12406e, #3d8fb8 55%, #1b4f6e); }
  .tile--hiking { left: 747px; top: 343px; background: linear-gradient(180deg, #b9cbd6, #6f8e4a 35%, #4e6b2c); }

  .features { position: absolute; left: 0; top: 608px; width: 1200px; height: 550px; }
  .features .title-videos { left: 390px; top: 38px; }
  .features .title-offers { left: 894px; top: 38px; }

  .video-main {
    position: absolute; left: 107px; top: 98px; width: 554px; height: 293px;
    background: linear-gradient(180deg, #5a82a8, #c3ccd4 30%, #6f8a8a 55%, #3d6e2a 75%, #2d3f2d);
  }
  .video-thumb { position: absolute; top: 404px; width: 179px; height: 109px; }
  .video-thumb--safari { left: 107px; background: linear-gradient(180deg, #a89a6a, #8c7a4a); }
  .video-thumb--coast { left: 294px; background: linear-gradient(180deg, #3e7ec4, #c9a87a 50%, #2d5a7a); }
  .video-thumb--canal { left: 482px; background: linear-gradient(180deg, #3a6e9a, #a0603a 55%, #1e3a4a); }
  .play {
    position: absolute; transform: translate(-50%, -50%);
  }

  .offer { position: absolute; width: 196px; height: 135px; overflow: hidden; }
  .offer--honeymoon { background: linear-gradient(180deg, #6c8db0, #3f5f82 60%, #2a4a5e); }
  .offer--family { background: linear-gradient(180deg, #8fb0c8, #4fb6c0 35%, #2a8a96 70%, #3a3a30); }
  .offer-name {
    position: absolute; left: 0; right: 0; top: 79px;
    text-align: center; color: var(--label-white);
    font-size: 13.5px; font-weight: 700; letter-spacing: -0.2px;
    text-shadow: 0 1px 3px rgba(0,0,0,0.7);
  }
  .offer-tag {
    position: absolute; left: 28px; top: 100px; width: 139px; height: 19px;
    background: var(--tag-yellow); color: var(--tag-ink);
    font-size: 13px; font-weight: 700; line-height: 19px; text-align: center;
  }
  .btn {
    position: absolute; top: 404px; width: 196px; height: 39px;
    color: var(--label-white); font-size: 14px; font-weight: 700;
    line-height: 39px; text-align: center; text-decoration: none;
  }
  .btn--book { left: 683px; background: var(--btn-book); }
  .btn--offers { left: 900px; background: var(--btn-offers); }

  .footer-band {
    position: absolute; left: 0; top: 1158px; width: 1200px; height: 42px;
    background: var(--band-grey);
  }
</style>
</head>
<body>
<div class="page">

  <section class="experiences">
    <h1 class="section-title"><strong>LUMEN GETAWAYS</strong> In less than 7 Days !</h1>

    <a class="tile tile--wildlife" role="img" aria-label="Photo of an elephant in green grassland">
      <span class="tile-shade"></span><span class="tile-label">Wonders of Wildlife</span>
    </a>
    <a class="tile tile--festivals" role="img" aria-label="Photo of a crowd at a colour powder festival">
      <span class="tile-shade"></span><span class="tile-label">World’s Greatest Festivals</span>
    </a>
    <a class="tile tile--activities" role="img" aria-label="Photo of a skater on an outdoor ice rink">
      <span class="tile-shade"></span><span class="tile-label">Must Do Activities</span>
    </a>
    <a class="tile tile--events" role="img" aria-label="Photo of a concert crowd with giant balloons">
      <span class="tile-shade"></span><span class="tile-label">Unique Annual Events</span>
    </a>
    <a class="tile tile--places" role="img" aria-label="Photo of a hiker beneath red sandstone cliffs">
      <span class="tile-shade"></span><span class="tile-label">Extraordinary &amp; Secret Places</span>
    </a>
    <a class="tile tile--performances" role="img" aria-label="Photo of dancers in blue dresses on stage">
      <span class="tile-shade"></span><span class="tile-label">Unforgettable Performances</span>
    </a>
    <a class="tile tile--hiking" role="img" aria-label="Photo of hikers walking across green hills">
      <span class="tile-shade"></span><span class="tile-label">Spectacular Hiking, Climbing<br>&amp; Walking</span>
    </a>
  </section>

  <section class="features">
    <h2 class="section-title title-videos">FEATURED <strong>VIDEOS</strong></h2>
    <h2 class="section-title title-offers">SPECIAL <strong>OFFERS</strong></h2>

    <div class="video-main" role="img" aria-label="Video still of houseboats on a palm-lined backwater">
      <svg class="play" style="left:286px;top:142px" width="38" height="38" viewBox="0 0 38 38" aria-hidden="true">
        <circle cx="19" cy="19" r="19" fill="var(--play-fill)"/>
        <path d="M15 11 L28 19 L15 27 Z" fill="var(--play-mark)"/>
      </svg>
    </div>
    <div class="video-thumb video-thumb--safari" role="img" aria-label="Video still of oryx on dry grassland">
      <svg class="play" style="left:89px;top:55px" width="24" height="24" viewBox="0 0 24 24" aria-hidden="true">
        <circle cx="12" cy="12" r="12" fill="var(--play-fill)"/>
        <path d="M9.5 7 L18 12 L9.5 17 Z" fill="var(--play-mark)"/>
      </svg>
    </div>
    <div class="video-thumb video-thumb--coast" role="img" aria-label="Video still of a traveller overlooking a coastal town">
      <svg class="play" style="left:89px;top:55px" width="24" height="24" viewBox="0 0 24 24" aria-hidden="true">
        <circle cx="12" cy="12" r="12" fill="var(--play-fill)"/>
        <path d="M9.5 7 L18 12 L9.5 17 Z" fill="var(--play-mark)"/>
      </svg>
    </div>
    <div class="video-thumb video-thumb--canal" role="img" aria-label="Video still of a canal city at dusk">
      <svg class="play" style="left:87px;top:55px" width="24" height="24" viewBox="0 0 24 24" aria-hidden="true">
        <circle cx="12" cy="12" r="12" fill="var(--play-fill)"/>
        <path d="M9.5 7 L18 12 L9.5 17 Z" fill="var(--play-mark)"/>
      </svg>
    </div>

    <a class="offer offer--honeymoon" style="left:684px;top:100px" role="img" aria-label="Photo of a couple by the sea">
      <span class="offer-name">Honeymoon Package</span><span class="offer-tag">20% DISCOUNT</span>
    </a>
    <a class="offer offer--family" style="left:902px;top:100px" role="img" aria-label="Photo of a family on a beach">
      <span class="offer-name">Family Package</span><span class="offer-tag">50% DISCOUNT</span>
    </a>
    <a class="offer offer--honeymoon" style="left:683px;top:256px" role="img" aria-label="Photo of a couple by the sea">
      <span class="offer-name">Honeymoon Package</span><span class="offer-tag">20% DISCOUNT</span>
    </a>
    <a class="offer offer--family" style="left:901px;top:256px" role="img" aria-label="Photo of a family on a beach">
      <span class="offer-name">Family Package</span><span class="offer-tag">50% DISCOUNT</span>
    </a>

    <a class="btn btn--book" href="#">BOOK YOUR TRIP</a>
    <a class="btn btn--offers" href="#">MORE OFFERS</a>
  </section>

  <div class="footer-band"></div>
</div>
</body>
</html>
```